Create an awesome website for a medical clinic

This is a new website for a doctor's office. The site should be clean and modern, easy to navigate.

This is a wellness clinic, we want to help our clients have a healthy, active lifestyle. It should be friendly and inviting, and easy for them to call or schedule an appointment.

The site should be responsive and designed using the attached Bootstrap 3 PSD.

We will provide stock photos, until then please use stock photos from:

pictovault.net or
imagebarrow.net (preferred)

Some example sites of clean and modern designs that we like:

https://tarvelspine.example/
http://quellmarrow.example/
http://brisklyhale.example/

Also attached is a temporary logo you can use.

Reason: Thank you everyone for your great designs - we need a little more time so I'm extending the project.

Need extra days to review

Also, the colors in the new logo I just linked to are the final colors of the logo, so feel free to use any complimentary colors to it.

Hi everyone, The boss wants to change the layout of the site a little bit - here's the revised layout: https://www.filecrate.example/s/k9pz31xq7vn84te/notes%2011_29_2017.pdf?dl=0 And the graphic assets you can use are here: https://www.filecrate.example/s/k9pz31xq7vn84te/notes%2011_29_2017.pdf?dl=0 Feel free to change the background color of the "topbar", and change the icons of the "why people trust us" if you want, these are just temporary placeholders. Thanks for your patience and hard work!

Target Market(s)

People seeking medical treatment (wellness clinic)

Industry/Entity Type

Doctor

Number of Pages Required

1 page

Font styles to use
Sans Serif

Colors
0592cd
33a6d7
abd037
9bcb3c

Requirements
Must have
• The home page should have: a strong hero image/slideshow, clinic phone number should be prominent and at the top of the page (in the nav), a "what to expect" section (this is like a FAQs section - see attachment), and a strong call to action (a button to call or schedule an appointment).
• The what to expect section is useful so that prospective clients can determine if we're a good fit for them or not. It's a basic, first-step pre-qualification block of information.
• Social media icons which links to our social media profiles should be included.
Nice to have
• - Link to 3 most recent blog entries
• - Testimonials
• - How a multilevel nav menu looks.

```html
<!DOCTYPE html>
<html lang="en">
<head>
<meta charset="utf-8">
<title>Verdant Medical Clinic</title>
<link href="https://fonts.googleapis.com/css2?family=Lato:ital,wght@0,300;0,400;0,700;0,900;1,400&display=swap" rel="stylesheet">
<style>
:root{
  --green:#43a047;
  --navy:#1f4e79;
  --ink:#333a40;
  --muted:#8a9097;
  --line:#e4e7ea;
  --footer:#1b2a3a;
}
*{box-sizing:border-box;margin:0;padding:0}
html,body{width:1200px;height:4569px;overflow:hidden}
body{position:relative;font-family:"Lato",Arial,sans-serif;color:var(--ink);background:#fff;font-size:13px}
.abs{position:absolute}
a{color:inherit;text-decoration:none}

/* top bar */
.topbar{left:0;top:0;width:1200px;height:46px;border-bottom:1px solid var(--line)}
.topbar .emergency{left:76px;top:15px;font-size:13px;font-weight:700;color:var(--navy)}
.socials{right:76px;top:13px;display:flex;gap:14px}
.socials span{width:20px;height:20px;border-radius:50%;background:#b9bec3;display:block}

/* nav */
.nav{left:0;top:46px;width:1200px;height:66px}
.brand{left:76px;top:23px;color:var(--ink);font-weight:700;font-size:17px;line-height:20px}
.menu{right:135px;top:25px;display:flex;gap:44px;font-size:13px;color:var(--ink)}
.search{right:76px;top:22px}

/* hero */
.hero{left:0;top:112px;width:1200px;height:552px;background:linear-gradient(90deg,#f6f7f8 0%,#eceef0 55%,#dfe4e8 100%)}
.hero-photo{left:330px;top:0;width:870px;height:552px;background:linear-gradient(90deg,rgba(236,238,240,0) 0%,#d7dde2 30%,#c9d2d8 60%,#dfe5ea 100%)}
.hero-kicker{left:76px;top:278px;color:#7a8590;font-size:15px}
.hero-title{left:76px;top:300px;width:480px;font-size:38px;line-height:44px;font-weight:400;color:var(--navy)}
.btn-outline{left:76px;top:410px;width:182px;height:50px;border-radius:25px;background:#fff;box-shadow:0 3px 10px rgba(0,0,0,.12);font-weight:700;font-size:13px;color:var(--navy);display:flex;align-items:center;justify-content:center;letter-spacing:.5px}

/* booking bar */
.booking{left:46px;top:636px;width:1108px;height:220px;background:var(--green);color:#fff}
.col-title{font-weight:700;font-size:14px;display:flex;align-items:center;gap:8px}
.hours{left:30px;top:40px;width:235px}
.hours table{margin-top:24px;width:100%;font-size:13px;border-collapse:collapse}
.hours td{padding:8px 0}
.hours td:last-child{text-align:right}
.contact{left:323px;top:40px}
.contact ul{list-style:none;margin-top:24px;font-size:13px}
.contact li{display:flex;align-items:center;gap:12px;padding:7px 0}
.visit{left:630px;top:40px;width:450px}
.field{position:absolute;height:34px;border:1.5px solid rgba(255,255,255,.85);border-radius:17px;font-size:11px;padding:10px 16px;color:#fff}
.send{position:absolute;height:34px;border-radius:17px;background:#fff;color:var(--green);font-weight:700;font-size:11px;display:flex;align-items:center;justify-content:center}

/* section headings */
.h-left{font-size:30px;font-weight:400;color:var(--navy)}
.h-left::after,.h-center::after{content:"";display:block;width:54px;height:3px;background:var(--green);margin-top:10px}
.h-center{width:1200px;text-align:center;font-size:30px;font-weight:400;color:var(--navy)}
.h-center::after{margin:10px auto 0}

/* about */
.about-bg{left:0;top:880px;width:1200px;height:695px;background:linear-gradient(90deg,#fff 55%,#f7f8f9 100%)}
.about-photo{left:731px;top:944px;width:426px;height:631px;background:linear-gradient(180deg,#f3f3f3,#e3e6ea 60%,#cfd6de)}
.about-text{left:76px;top:1030px;width:510px;font-size:13px;line-height:18px;color:#555}
.quote{left:76px;top:1116px;font-size:28px;color:var(--navy);font-weight:300}
.acc-item{left:76px;width:510px}
.acc-head{display:flex;align-items:center;gap:16px;font-weight:700;font-size:15px;color:var(--navy)}
.acc-head .arrow{margin-left:auto}
.acc-body{margin:14px 0 0 46px;font-size:12px;line-height:17px;color:#555}

/* facilities */
.facility{top:1730px;width:160px;text-align:center}
.facility svg{display:block;margin:0 auto}
.facility h3{font-size:17px;font-weight:400;color:var(--ink);margin-top:26px}
.facility p{font-size:12px;line-height:15px;color:#777;margin-top:10px}
.facility.active .card{position:absolute;left:12px;top:-28px;width:150px;height:210px;background:#fff;box-shadow:0 4px 18px rgba(0,0,0,.12)}

/* stats */
.stats{left:0;top:2001px;width:1200px;height:180px;background:var(--green);color:#fff}
.stat{top:58px;width:200px;text-align:center}
.stat b{display:block;font-size:31px;font-weight:700}
.stat span{font-size:13px}

/* news */
.news-card{top:2348px;width:241px;height:369px;background:#fff;box-shadow:0 2px 12px rgba(0,0,0,.08)}
.news-img{width:241px;height:186px}
.news-card h3{margin:24px 18px 0;font-size:17px;font-weight:700;color:var(--navy)}
.news-card .date{margin:8px 18px 0;font-size:12px;color:#777}
.news-card p{margin:14px 18px 0;font-size:12px;line-height:16px;color:#666}
.news-card .go{position:absolute;left:18px;bottom:18px}

/* testimonials */
.testi-bg{left:0;top:2905px;width:1200px;height:308px;background:linear-gradient(90deg,#f1f2f3,#f7f8f9 60%,#eef0f2)}
.testi-photo{left:624px;top:2875px;width:503px;height:338px;background:linear-gradient(180deg,rgba(230,233,236,0),#d6dbe0 40%,#c7ced5)}
.testi-head{left:76px;top:2922px;font-size:45px;line-height:50px;font-weight:900;color:var(--navy);letter-spacing:.5px}
.quote-mark{left:584px;top:2918px}
.testi-text{left:76px;top:3042px;width:420px;font-size:12.5px;line-height:17px;font-style:italic;color:#8a9097}
.testi-name{left:76px;top:3138px;font-size:13px;color:var(--navy)}
.testi-name small{font-size:10px;color:#8a9097;margin-left:6px}
.dots{left:76px;top:3172px;display:flex;gap:10px}
.dots span{width:11px;height:11px;border-radius:50%;background:#c9ced3}
.dots span.on{background:#2f7fc0}

/* faq */
.faq{left:76px;width:1048px;background:#fff;box-shadow:0 2px 14px rgba(0,0,0,.08);padding:0 36px}
.faq h4{font-size:15px;font-weight:700;color:var(--navy);display:flex;align-items:center;height:73px}
.faq h4 svg{margin-left:auto}
.faq.open h4{height:66px}
.faq p{font-size:12px;line-height:16px;color:#555;margin-top:-10px}

/* map & footer */
.map{left:0;top:4015px;width:1200px;height:499px;background:linear-gradient(135deg,#e9eaeb,#dfe1e3 50%,#e6e7e8)}
.footer{left:0;top:4514px;width:1200px;height:55px;background:var(--footer);color:#fff;font-size:14px;font-weight:700;display:flex;align-items:center;justify-content:center}
</style>
</head>
<body>

<header>
  <div class="abs topbar">
    <div class="abs emergency">For Emergency call 111.555.0142</div>
    <div class="abs socials" aria-label="Social media profiles"><span></span><span></span><span></span><span></span></div>
  </div>
  <nav class="abs nav">
    <div class="abs brand">Verdant Medical Clinic</div>
    <div class="abs menu"><a>About Me</a><a>Medical Services</a><a>Departments</a><a>What to Expect</a><a>Contact</a></div>
    <svg class="abs search" width="20" height="20" viewBox="0 0 20 20"><circle cx="8" cy="8" r="6" fill="none" stroke="#b0b6bc" stroke-width="1.8"/><line x1="12.5" y1="12.5" x2="18" y2="18" stroke="#b0b6bc" stroke-width="1.8"/></svg>
  </nav>
</header>

<section class="abs hero">
  <div class="abs hero-photo" role="img" aria-label="Photo of a smiling team of doctors in white coats"></div>
  <div class="abs hero-kicker">Suas munere corrumpit te quo</div>
  <h1 class="abs hero-title">Persius ponderum honestati squod postea vocent</h1>
  <a class="abs btn-outline">WHAT TO EXPECT</a>
</section>

<section class="abs booking">
  <div class="abs hours">
    <div class="col-title"><svg width="14" height="14" viewBox="0 0 14 14"><circle cx="7" cy="7" r="6" fill="#fff"/><path d="M7 3.5V7l2.5 1.5" stroke="#43a047" stroke-width="1.5" fill="none"/></svg>Working Time</div>
    <table>
      <tr><td>Monday - Friday</td><td>8.00 - 17.00</td></tr>
      <tr><td>Saturday</td><td>9.30 - 17.30</td></tr>
      <tr><td>Sunday</td><td>9.30 - 15.00</td></tr>
    </table>
  </div>
  <div class="abs contact">
    <div class="col-title"><svg width="14" height="14" viewBox="0 0 14 14"><path d="M3 1l2.5 3-1.5 1.5c.8 1.8 2 3 3.7 3.8L9.2 7.8 12.5 10 11 13C6 12.5 1.5 8 1 3z" fill="#fff"/></svg>Contact Us</div>
    <ul>
      <li><svg width="12" height="12" viewBox="0 0 14 14"><path d="M3 1l2.5 3-1.5 1.5c.8 1.8 2 3 3.7 3.8L9.2 7.8 12.5 10 11 13C6 12.5 1.5 8 1 3z" fill="#fff"/></svg>111.555.0142</li>
      <li><svg width="12" height="12" viewBox="0 0 12 12"><rect x="0.5" y="2" width="11" height="8" fill="#fff"/><path d="M1 2.5l5 4 5-4" stroke="#43a047" fill="none"/></svg>contact@verdantclinic.example</li>
      <li><svg width="12" height="12" viewBox="0 0 12 12"><path d="M1 6L6 1.5 11 6H9.5v5h-7V6z" fill="#fff"/></svg>48 Larkmoor St Fairhaven, NY 10999</li>
    </ul>
  </div>
  <div class="abs visit">
    <div class="col-title"><svg width="12" height="14" viewBox="0 0 12 14"><path d="M6 0a5 5 0 0 1 5 5c0 3.5-5 9-5 9S1 8.5 1 5a5 5 0 0 1 5-5z" fill="#fff"/><circle cx="6" cy="5" r="1.8" fill="#43a047"/></svg>Booking a visit</div>
    <div class="field" style="left:0;top:38px;width:145px">Full Name</div>
    <div class="field" style="left:162px;top:38px;width:145px">Phone</div>
    <div class="field" style="left:324px;top:38px;width:126px">Date of Birth</div>
    <div class="field" style="left:0;top:90px;width:307px">Reason</div>
    <div class="send" style="left:324px;top:90px;width:126px">SEND</div>
  </div>
</section>

<section class="about">
  <div class="abs about-bg"></div>
  <div class="abs about-photo" role="img" aria-label="Photo of a smiling doctor with a stethoscope holding a clipboard"></div>
  <h2 class="abs h-left" style="left:76px;top:955px">About Me</h2>
  <p class="abs about-text">Id mollis instructior sit, his fuisset democritum ex, nibh docendi legendos ne sit. Eum diceret inductum eam Persius ponor sit, his fuisset democritum ex, nibh docendi legendos neum derum honestatis vel ad, quod postea vocent no vel.</p>
  <div class="abs quote">“Health is the most preciuos treasure”</div>
  <div class="abs acc-item" style="top:1195px">
    <div class="acc-head"><svg width="28" height="28" viewBox="0 0 28 28"><path d="M14 3l9 3v7c0 6-4 10-9 12-5-2-9-6-9-12V6z" fill="#2f6fa8"/><path d="M14 9v9M9.5 13.5h9" stroke="#fff" stroke-width="2.4"/></svg>Experienced Physician<svg class="arrow" width="12" height="14" viewBox="0 0 12 14"><path d="M6 13V2M1.5 6L6 1.5 10.5 6" stroke="#8a9097" stroke-width="1.4" fill="none"/></svg></div>
    <p class="acc-body">lorem ipsum dolor sit amet, cu decore efficiantur vis, possim melius vel at. Ei vidisse minimum incidererit mei, an usu consequat voluptatibus nec, eos pa rhen placerat disputationi m. Justo dicant doctus sed in, sit putent diceret an, ludus ubique no nam. In veri decore dictas sit, nam eu nisl possit, pri erat placerat patrioque id.</p>
  </div>
  <div class="abs acc-item" style="top:1385px">
    <div class="acc-head"><svg width="28" height="28" viewBox="0 0 28 28"><rect x="4" y="11" width="20" height="6" rx="3" transform="rotate(-40 14 14)" fill="#2f6fa8"/><line x1="3" y1="25" x2="8" y2="20" stroke="#2f6fa8" stroke-width="2"/></svg>Complete Health Facilities<svg class="arrow" width="14" height="12" viewBox="0 0 14 12"><path d="M1 6h11M8 1.5L12.5 6 8 10.5" stroke="#8a9097" stroke-width="1.4" fill="none"/></svg></div>
  </div>
  <div class="abs acc-item" style="top:1468px">
    <div class="acc-head"><svg width="28" height="28" viewBox="0 0 28 28"><rect x="3" y="5" width="22" height="15" rx="1.5" fill="#2f6fa8"/><rect x="10" y="21" width="8" height="3" fill="#2f6fa8"/><path d="M6 13h4l2-4 3 7 2-3h4" stroke="#fff" stroke-width="1.6" fill="none"/></svg>Medical Standard Equipment<svg class="arrow" width="14" height="12" viewBox="0 0 14 12"><path d="M1 6h11M8 1.5L12.5 6 8 10.5" stroke="#8a9097" stroke-width="1.4" fill="none"/></svg></div>
  </div>
</section>

<section class="facilities">
  <h2 class="abs h-center" style="left:0;top:1643px">Facilities</h2>
  <div class="abs facility" style="left:71px">
    <svg width="80" height="80" viewBox="0 0 80 80"><rect x="8" y="28" width="44" height="22" rx="11" transform="rotate(-45 30 39)" fill="var(--green)"/><circle cx="56" cy="52" r="16" fill="var(--green)"/><line x1="45" y1="63" x2="67" y2="41" stroke="#fff" stroke-width="3"/></svg>
    <h3>Medicines</h3><p>Id mollis instructior<br>sit, his fuisset</p>
  </div>
  <div class="abs facility" style="left:251px">
    <svg width="80" height="80" viewBox="0 0 80 80"><path d="M40 70C20 55 6 43 6 27a17 17 0 0 1 34-4 17 17 0 0 1 34 4c0 16-14 28-34 43z" fill="var(--green)"/><path d="M10 38h18l5-10 7 18 5-8h25" stroke="#fff" stroke-width="3" fill="none"/></svg>
    <h3>Best Care</h3><p>Id mollis instructior<br>sit, his fuisset</p>
  </div>
  <div class="abs facility" style="left:431px">
    <svg width="80" height="80" viewBox="0 0 80 80"><rect x="30" y="10" width="20" height="10" rx="2" fill="none" stroke="var(--green)" stroke-width="4"/><rect x="8" y="20" width="64" height="48" rx="5" fill="var(--green)"/><path d="M40 32v24M28 44h24" stroke="#fff" stroke-width="6"/></svg>
    <h3>Research</h3><p>Id mollis instructior<br>sit, his fuisset</p>
  </div>
  <div class="abs facility active" style="left:611px">
    <div class="card"></div>
    <svg style="position:relative" width="80" height="80" viewBox="0 0 80 80"><rect x="6" y="18" width="6" height="50" fill="var(--green)"/><rect x="68" y="40" width="6" height="28" fill="var(--green)"/><rect x="6" y="50" width="68" height="6" fill="var(--green)"/><circle cx="22" cy="42" r="6" fill="var(--green)"/><rect x="32" y="38" width="38" height="10" rx="3" fill="var(--green)"/><path d="M46 16v16M38 24h16" stroke="var(--green)" stroke-width="5"/></svg>
    <h3 style="position:relative">Bed Facility</h3><p style="position:relative">Id mollis instructior<br>sit, his fuisset</p>
  </div>
  <div class="abs facility" style="left:791px">
    <svg width="80" height="80" viewBox="0 0 80 80"><rect x="24" y="6" width="32" height="10" rx="2" fill="var(--green)"/><rect x="18" y="20" width="44" height="54" rx="5" fill="var(--green)"/><rect x="18" y="34" width="44" height="24" fill="#fff" opacity=".25"/><path d="M40 36v20M30 46h20" stroke="#fff" stroke-width="5"/></svg>
    <h3>Safe Medication</h3><p>Id mollis instructior<br>sit, his fuisset</p>
  </div>
  <div class="abs facility" style="left:971px">
    <svg width="80" height="80" viewBox="0 0 80 80"><rect x="18" y="12" width="44" height="62" rx="4" fill="var(--green)"/><rect x="30" y="6" width="20" height="12" rx="3" fill="var(--green)"/><path d="M28 34h24M28 44h24M28 54h24" stroke="#fff" stroke-width="3.5"/></svg>
    <h3>Reports</h3><p>Id mollis instructior<br>sit, his fuisset</p>
  </div>
</section>

<section class="abs stats">
  <div class="abs stat" style="left:104px"><b>200%</b><span>Trustworthy</span></div>
  <div class="abs stat" style="left:369px"><b>2451</b><span>Patients in a year</span></div>
  <div class="abs stat" style="left:630px"><b>215</b><span>Awards Won</span></div>
  <div class="abs stat" style="left:893px"><b>24</b><span>Years of Experience</span></div>
</section>

<section class="news">
  <h2 class="abs h-center" style="left:0;top:2252px">Latest News</h2>
  <article class="abs news-card" style="left:76px">
    <div class="news-img" role="img" aria-label="Photo of swings in a leafy park" style="background:linear-gradient(180deg,#7d8f62,#5e6d4a 60%,#8a8670)"></div>
    <h3>First day in hospital</h3><div class="date">10 Dec, 2017</div>
    <p>Eum diceret inductum ei. Persius ponderum honestatis vel ad, quod postea vocent no vel...</p>
    <svg class="go" width="16" height="12" viewBox="0 0 16 12"><path d="M1 6h13M9.5 1.5L14 6 9.5 10.5" stroke="#555" stroke-width="1.4" fill="none"/></svg>
  </article>
  <article class="abs news-card" style="left:344px">
    <div class="news-img" role="img" aria-label="Photo of a young girl outdoors" style="background:linear-gradient(180deg,#6f8f4e,#a08f7a 60%,#c5ad96)"></div>
    <h3>First day in hospital</h3><div class="date">10 Dec, 2017</div>
    <p>Eum diceret inductum ei. Persius ponderum honestatis vel ad, quod postea vocent no vel...</p>
    <svg class="go" width="16" height="12" viewBox="0 0 16 12"><path d="M1 6h13M9.5 1.5L14 6 9.5 10.5" stroke="#555" stroke-width="1.4" fill="none"/></svg>
  </article>
  <article class="abs news-card" style="left:615px">
    <div class="news-img" role="img" aria-label="Photo of a child standing in a garden" style="background:linear-gradient(180deg,#3f6a2c,#5b8238 55%,#2e3a25)"></div>
    <h3>First day in hospital</h3><div class="date">10 Dec, 2017</div>
    <p>Eum diceret inductum ei. Persius ponderum honestatis vel ad, quod postea vocent no vel...</p>
    <svg class="go" width="16" height="12" viewBox="0 0 16 12"><path d="M1 6h13M9.5 1.5L14 6 9.5 10.5" stroke="#555" stroke-width="1.4" fill="none"/></svg>
  </article>
  <article class="abs news-card" style="left:883px">
    <div class="news-img" role="img" aria-label="Photo of a hand holding a test tube over blue water" style="background:linear-gradient(180deg,#9cc6dc,#2f8ea8 55%,#1e6f86)"></div>
    <h3>First day in hospital</h3><div class="date">10 Dec, 2017</div>
    <p>Eum diceret inductum ei. Persius ponderum honestatis vel ad, quod postea vocent no vel...</p>
    <svg class="go" width="16" height="12" viewBox="0 0 16 12"><path d="M1 6h13M9.5 1.5L14 6 9.5 10.5" stroke="#555" stroke-width="1.4" fill="none"/></svg>
  </article>
</section>

<section class="testimonials">
  <h2 class="abs h-left" style="left:76px;top:2825px">Testimonials</h2>
  <div class="abs testi-bg"></div>
  <div class="abs testi-photo" role="img" aria-label="Photo of a happy patient in a shirt and tie giving two thumbs up"></div>
  <div class="abs testi-head">KEEP YOUR HEAD UP<br>AND BE PATIENT</div>
  <svg class="abs quote-mark" width="66" height="56" viewBox="0 0 66 56"><path d="M4 4h24v22L18 52H8l8-26H4zM38 4h24v22L52 52H42l8-26H38z" fill="#c9ced4"/></svg>
  <p class="abs testi-text">Justo dicant doctus sed in, sit putent diceret an, ludus ubique no nam In veri decore dictas sit, nam eu nisl possit, pri erat placerat mollis instructior sit, his fuisset democritum ex, nibh docendi legendos ne</p>
  <div class="abs testi-name">Owen Hartley<small>Happy Patient</small></div>
  <div class="abs dots"><span></span><span></span><span class="on"></span><span></span></div>
  <svg class="abs" style="left:226px;top:3172px" width="16" height="12" viewBox="0 0 16 12"><path d="M1 6h13M9.5 1.5L14 6 9.5 10.5" stroke="#555" stroke-width="1.4" fill="none"/></svg>
</section>

<section class="faqs">
  <h2 class="abs h-center" style="left:0;top:3285px">FAQ</h2>
  <div class="abs faq open" style="top:3366px;height:152px">
    <h4>Id mollis instructior sit, his fuisset democritum ex, nibh docendi legendos ne sit?<svg width="12" height="14" viewBox="0 0 12 14"><path d="M6 13V2M1.5 6L6 1.5 10.5 6" stroke="#8a9097" stroke-width="1.4" fill="none"/></svg></h4>
    <p>Justo dicant doctus sed in, sit putent diceret an, ludus ubique no nam. In veri decore dictas sit, nam eu nisl possit, pri erat placerat patrioque id. Id mollis instructior sit, his fuisset democritum ex, nibh docendi legendos ne sit. Eum diceret inductum ei. Persius ponderum honestatis vel ad, quod postea vocent no vel. Omnis suavitate adversarium quo ea. Cu eos mucius aliquid corpora.</p>
  </div>
  <div class="abs faq" style="top:3552px;height:73px"><h4>Eu cum eligendi voluptua perfecto. No brute laboramus reprehendunt pri, et sint ponderum quo?<svg width="14" height="12" viewBox="0 0 14 12"><path d="M1 6h11M8 1.5L12.5 6 8 10.5" stroke="#8a9097" stroke-width="1.4" fill="none"/></svg></h4></div>
  <div class="abs faq" style="top:3652px;height:73px"><h4>Quo omnis voluptaria ut, causae habemus ius at. Duo in etiam numquam lobortis, sed ne eligendi cotidieque?<svg width="14" height="12" viewBox="0 0 14 12"><path d="M1 6h11M8 1.5L12.5 6 8 10.5" stroke="#8a9097" stroke-width="1.4" fill="none"/></svg></h4></div>
  <div class="abs faq" style="top:3753px;height:73px"><h4>Suas munere corrumpit te quo, duo salutatus voluptatibus definitionem at?<svg width="14" height="12" viewBox="0 0 14 12"><path d="M1 6h11M8 1.5L12.5 6 8 10.5" stroke="#8a9097" stroke-width="1.4" fill="none"/></svg></h4></div>
  <div class="abs faq" style="top:3853px;height:73px"><h4>Justo dicant doctus sed in, sit putent diceret an, ludus ubique no nam. In veri decore dictas sit, nam eu nisl?<svg width="14" height="12" viewBox="0 0 14 12"><path d="M1 6h11M8 1.5L12.5 6 8 10.5" stroke="#8a9097" stroke-width="1.4" fill="none"/></svg></h4></div>
</section>

<div class="abs map" role="img" aria-label="Street map of the clinic neighbourhood with a blue location pin"></div>

<footer class="abs footer">© 2017 Copyright Verdant</footer>

</body>
</html>
```